AVOID HOT “HARISSA” SAUCE. IN CAN

Brand Overview: Create a dynamic and eye-catching label for our new hot sauce IN CAN, “DUMEL.” Our brand is all about delivering a fiery flavor experience that combines the intensity of various peppers with unique, bold ingredients. The hot sauce targets spice enthusiasts who crave both heat and distinctive taste profiles.

Key Messages: Intensity: Emphasize the extreme heat level of the hot sauce to appeal to spice lovers.
Traditional: The taste is traditional
Flavor Fusion: Highlight the unique blend of peppers and special ingredients that sets DUMEL

Quality Ingredients: Convey the use of premium, natural ingredients to reinforce the high-quality aspect of our product.

Versatility: Communicate the sauce's versatility – perfect for various cuisines and dishes. Design Elements:

Color Palette: Use fiery reds, oranges, and yellows to convey the heat, with accents of dark and smoky tones to suggest depth of flavor.

Typography: Choose bold and legible fonts for the product name, ensuring it is easily readable from a distance.
Imagery: Incorporate visuals of flaming peppers or a stylized fire to reinforce the spicy nature of the hot sauce.
Consider using images of the key ingredients to showcase the fusion of flavors.

Texture/Background: Add a textured or gradient background to enhance visual interest and give a sense of depth.

Label Information: Product Name Hot Sauce "HARISSA" Heat Level

Indicator: Use a visual scale or iconography to indicate the spiciness level.

Ingredients: Highlight key ingredients and emphasize their quality, peppers, water, salt
SIZE: L: 12cm H: 5.5cm

Net Weight: 140g

Regulatory Information: Ensure compliance with all relevant food labeling regulations, including ingredients list, nutritional information, and contact details.

Competitor Analysis: Examine other hot sauce labels in the market to identify design trends and differentiators.
Inspiration: Consider drawing inspiration from elements like flames, peppers, or global spice motifs to create a visually striking and memorable label. Mood/Emotion: The label should evoke excitement, daring, and a sense of adventure – capturing the thrill of experiencing the intense flavor of HARISSA DUMEL Hot Sauce.

Target Audience: Spice enthusiasts, foodies, and individuals seeking a unique and bold addition to their culinary experiences.

Delivery Format: The label design should be suitable for various packaging sizes, ensuring scalability without sacrificing visual impact. Remember to balance the vibrant and intense visuals with clarity and readability and send the FONT at the moment of the delivery.
Updates

Need extra days to review

Target Market(s)

European

Font styles to use
Decorative

Colors
FFF300
FFF600
FEFA6F
FFFEC7
FFFEE8
FFC000
F8CF3A
FAE287
FDF2CF
FEFAEE
EE7325
F08F49
F5BC92
FAE3D3
FDF4ED
EB3D1F
EC4F4E
F09395
F8D3D4
FCEDEE

Requirements
Must have
• LOGO, BARCODE, Nutritional facts, INGREDIENTS

```html
<!DOCTYPE html>
<html lang="en">
<head>
<meta charset="UTF-8">
<title>DUMEL Harissa Hot Sauce Label</title>
<link href="https://fonts.googleapis.com/css2?family=Montserrat:wght@500;700&family=Rye&display=swap" rel="stylesheet">
<style>
  :root {
    --page-bg: #dcdcdc;
    --label-black: #141414;
    --label-dark: #1c1212;
    --smoke: #2a1512;
    --ember: #7a1a0e;
    --flame-red: #eb3d1f;
    --flame-orange: #ee7325;
    --flame-glow: #f08f49;
    --pepper-red: #d8170f;
    --pepper-deep: #a80d08;
    --text-white: #f2f2f2;
    --accent-red: #e0281f;
    --brand-blue: #35386e;
  }
  * { margin: 0; padding: 0; box-sizing: border-box; }
  html, body {
    width: 1200px;
    height: 800px;
    overflow: hidden;
    background: var(--page-bg);
  }
  .label {
    position: absolute;
    left: 360px;
    top: 80px;
    width: 480px;
    height: 640px;
    overflow: hidden;
    background: linear-gradient(180deg, var(--label-black) 0%, var(--label-dark) 45%, var(--smoke) 62%, var(--ember) 100%);
  }
  .spice-pattern {
    position: absolute;
    inset: 0 0 35% 0;
    background: radial-gradient(ellipse at 50% 40%, rgba(90, 20, 20, 0.18), rgba(20, 20, 20, 0) 70%);
  }
  .flames {
    position: absolute;
    left: 0;
    right: 0;
    bottom: 0;
    height: 300px;
    background:
      radial-gradient(ellipse at 50% 85%, var(--flame-glow) 0%, var(--flame-orange) 22%, var(--flame-red) 45%, rgba(122, 26, 14, 0.6) 70%, rgba(122, 26, 14, 0) 100%);
  }
  .brand {
    position: absolute;
    top: 92px;
    left: 0;
    right: 0;
    display: flex;
    justify-content: center;
    align-items: center;
    gap: 12px;
  }
  .brand-mark {
    width: 18px;
    height: 18px;
    background: var(--brand-blue);
  }
  .brand-name {
    font-family: "Montserrat", sans-serif;
    font-weight: 700;
    font-size: 46px;
    letter-spacing: 2px;
    color: var(--text-white);
  }
  .product-type {
    position: absolute;
    top: 252px;
    left: 0;
    right: 0;
    text-align: center;
    font-family: "Montserrat", sans-serif;
    font-weight: 500;
    font-size: 24px;
    letter-spacing: 8px;
    color: var(--accent-red);
  }
  .product-name {
    position: absolute;
    top: 288px;
    left: 0;
    right: 0;
    text-align: center;
    font-family: "Rye", serif;
    font-size: 72px;
    letter-spacing: 2px;
    color: var(--text-white);
  }
  .pepper {
    position: absolute;
    left: 92px;
    top: 390px;
    width: 320px;
    height: 150px;
    border-radius: 0 0 160px 160px / 0 0 150px 150px;
    background: radial-gradient(ellipse at 45% 35%, var(--pepper-red) 0%, var(--pepper-red) 50%, var(--pepper-deep) 100%);
  }
  .net-weight {
    position: absolute;
    bottom: 26px;
    left: 0;
    right: 0;
    text-align: center;
    font-family: "Montserrat", sans-serif;
    font-weight: 700;
    font-size: 17px;
    color: var(--text-white);
  }
</style>
</head>
<body>
  <main class="label">
    <div class="spice-pattern" role="img" aria-label="Faint outline pattern of chili peppers and garlic bulbs"></div>
    <div class="flames" role="img" aria-label="Stylized orange and red fire rising from the bottom of the label"></div>

    <div class="brand">
      <span class="brand-mark"></span>
      <span class="brand-name">DUMEL</span>
    </div>

    <p class="product-type">HOT SAUCE</p>
    <h1 class="product-name">HARISSA</h1>

    <div class="pepper" role="img" aria-label="Glossy red chili pepper with a green stem lying above the flames"></div>

    <p class="net-weight">140g</p>
  </main>
</body>
</html>
```